Bref créative
Brightfield pest control
Stationary business card project for brightfield pest control
Professional
Doug Harlan
4120 w pinecrest ln. meridian idaho 83619
dharlan77@mailvista.net
ALL SERVICES GUARANTEED
Residential.Commercial Service.Certified specialist.Free Estimates
This is the company logo.

```html
<!DOCTYPE html>
<html lang="en">
<head>
<meta charset="utf-8">
<title>Brightfield pest control – business card</title>
<link href="https://fonts.googleapis.com/css2?family=Arimo:wght@400;700&display=swap" rel="stylesheet">
<style>
  :root {
    --backdrop: #e8e5e0;
    --card: #ffffff;
    --ink: #111111;
    --green: #3fa535;
    --green-dark: #2e7d2a;
    --green-light: #cfe6b8;
  }
  * { margin: 0; padding: 0; box-sizing: border-box; }
  html, body {
    width: 1200px;
    height: 802px;
    overflow: hidden;
    background: var(--backdrop);
    font-family: "Arimo", Arial, sans-serif;
    color: var(--ink);
  }
  .card {
    position: absolute;
    left: 100px;
    top: 100px;
    width: 1000px;
    height: 604px;
    background: var(--card);
    border-radius: 30px;
    overflow: hidden;
    box-shadow: 0 4px 14px rgba(0,0,0,0.15);
  }
  .brand {
    position: absolute;
    left: 70px;
    top: 230px;
    width: 330px;
    display: flex;
    align-items: center;
    gap: 16px;
  }
  .brand-dot {
    flex: none;
    width: 34px;
    height: 34px;
    border-radius: 50%;
    background: var(--green);
  }
  .brand-name {
    font-weight: 700;
    font-size: 40px;
    line-height: 1.1;
    color: var(--green);
  }
  .divider {
    position: absolute;
    left: 466px;
    top: 60px;
    width: 3px;
    height: 420px;
    background: var(--green);
  }
  .contact {
    position: absolute;
    left: 482px;
    top: 128px;
  }
  .contact-name {
    font-size: 44px;
    font-weight: 400;
    margin-bottom: 30px;
  }
  .contact-line {
    font-size: 22px;
    line-height: 34px;
  }
  .services {
    position: absolute;
    right: 22px;
    top: 490px;
    text-align: right;
  }
  .services-title {
    font-size: 28px;
    font-weight: 700;
    letter-spacing: 0.5px;
  }
  .services-list {
    font-size: 15px;
    margin-top: 4px;
    letter-spacing: -0.2px;
  }
  .band {
    position: absolute;
    left: 0;
    right: 0;
    top: 552px;
    height: 16px;
    background: linear-gradient(90deg, var(--green-dark) 0%, var(--green) 45%, var(--green-light) 100%);
  }
</style>
</head>
<body>
  <div class="card">
    <div class="brand">
      <span class="brand-dot"></span>
      <span class="brand-name">brightfield pest control</span>
    </div>

    <div class="divider"></div>

    <div class="contact">
      <p class="contact-name">Doug Harlan</p>
      <p class="contact-line">A: 4120 w pinecrest ln. meridian idaho 83619</p>
      <p class="contact-line">C: (208)555-0137</p>
      <p class="contact-line">E: dharlan77@mailvista.net</p>
    </div>

    <div class="services">
      <p class="services-title">ALL SERVICES GUARANTEED</p>
      <p class="services-list">Residential.Commercial Service.Certified specialist.Free Estimates</p>
    </div>

    <div class="band"></div>
  </div>
</body>
</html>
```